Eftpos Comparison Site requires banner adds

At QuoteNest.com.au we are a free service that allows our customers to get up to five quotes from our panel of suppliers for a range of BUSINESS related products and services. These products include eftpos / credit card machines, bank accounts, insurance, signage,office furniture etc. basically anything that a small business would need.
The process is done in 3 steps; 1) register your enquiry 2) we source and provide the five cheapest quotes 3) then select the supplier of your choice,the process is simple 123 and is FREE.

Please visit the soon to be revamped website to see our current horrible banner adds.
I require 8 banner adds with the below information
ADD 1) Get up to 10 quotes here FREE
Add 2) Australia's only EFTPOS comparison site
Add 3) Ringing everywhere for quotes.............it's so yesterday!
Add 4) Hate Eftpos Fee? Eftpos surcharging now available.
Add 5) Eftpos eating your profits? Let us put your Eftpos on a diet
Add 6) Pay less for "Norva logo" "Pelliworth Logo" "Eftpos Logo"
Add 7) Get "Flick to Buy" now
Add 8) We guarantee to get you a better deal than your bank!

Reason: I am extending your deadline because there are 8 banners and i dont want to rush you given that you have so many designs to work on.

Target Market(s)

small and medium business operators

Industry/Entity Type

Small Business

Requirements
Must have
• must have images and be bold

```html
<!DOCTYPE html>
<html lang="en">
<head>
<meta charset="UTF-8">
<title>QuoteNest – EFTPOS eating your profits?</title>
<link rel="stylesheet" href="https://fonts.googleapis.com/css2?family=Bebas+Neue&family=Arial&display=swap">
<style>
  :root {
    --purple-light: #8356a8;
    --purple-mid: #6c3d95;
    --purple-deep: #56287c;
    --white: #ffffff;
    --yellow: #f6e500;
    --plate-dark: #1a1420;
    --plate-pink: #e98fb8;
  }
  html, body {
    margin: 0;
    padding: 0;
    overflow: hidden;
    background: var(--purple-deep);
  }
  .banner {
    position: relative;
    width: 1200px;
    height: 304px;
    overflow: hidden;
    background: radial-gradient(ellipse at 50% 40%, var(--purple-light) 0%, var(--purple-mid) 55%, var(--purple-deep) 100%);
    font-family: "Bebas Neue", "Arial Narrow", sans-serif;
  }
  .brand {
    position: absolute;
    left: 16px;
    top: 10px;
    display: flex;
    align-items: center;
    gap: 6px;
    color: var(--white);
    font-size: 24px;
    line-height: 1;
    letter-spacing: 0.5px;
  }
  .brand-dot {
    width: 14px;
    height: 14px;
    border-radius: 50%;
    background: var(--white);
  }
  .headline {
    position: absolute;
    margin: 0;
    font-weight: 400;
    text-transform: uppercase;
    line-height: 0.9;
  }
  .headline--question {
    left: 20px;
    top: 86px;
    color: var(--white);
    font-size: 80px;
    letter-spacing: 1px;
  }
  .headline--offer {
    left: 792px;
    top: 98px;
    color: var(--yellow);
    font-size: 68px;
    letter-spacing: 1px;
  }
  .table-setting {
    position: absolute;
    left: 438px;
    top: 42px;
    width: 336px;
    height: 226px;
    border-radius: 8px;
    background: radial-gradient(ellipse at 50% 50%, var(--plate-pink) 0%, #a0577e 22%, var(--plate-dark) 45%, #3a2a46 70%, rgba(108, 61, 149, 0) 100%);
  }
</style>
</head>
<body>
  <div class="banner">
    <div class="brand"><span class="brand-dot"></span>QuoteNest.com.au</div>

    <h1 class="headline headline--question">EFTPOS eating<br>your profits?</h1>

    <div class="table-setting" role="img" aria-label="Pink piggy bank sitting on a black dinner plate between a fork and a knife"></div>

    <h2 class="headline headline--offer">Let us put your<br>EFTPOS on a diet</h2>
  </div>
</body>
</html>
```